8"x5" postcard for Wireless Internet introduction to new mountain town market

I need to market high speed internet to a resort mountain town without doing the obvious laptop on a mountain top thing, so tired. We are going to be competing directly with another provider with same cost, but we will be offering free installation. The area is Aspen Colorado, so the clientele are outdoor types who have suffered for years from being disconnected in their mountain town. We offer fast internet and excellent customer service from people who live in their neck of the woods.

Target Market(s)

23-55 years old, both resort living, families and ski bums

Font styles to use
Sans Serif

Colors

Designer to choose colors to be used in the design.

Requirements
Must have
• Visual appeal and fresh verbiage. We don't mind being a little edgy. We are a young company and we want to appeal to people looking for a provider who gets them. We prefer a clean look.
Nice to have
• Nice to have colors that match our logo
Should not have
• stuffy concepts or verbiage that is too much like a car salesman. We don't want to look like a 'big box' company.

```html
<!DOCTYPE html>
<html lang="en">
<head>
<meta charset="UTF-8">
<title>Summitline Broadband – Postcard 3</title>
<link href="https://fonts.googleapis.com/css2?family=Montserrat:wght@800&family=Roboto:wght@300;400;500&display=swap" rel="stylesheet">
<style>
  :root {
    --sheet: #f2f2f2;
    --card: #ffffff;
    --sun: #fbc02d;
    --ink: #222222;
    --slate: #666666;
    --mist: #8a8a8a;
    --rule: #2a2a2a;
  }
  * { margin: 0; padding: 0; box-sizing: border-box; }
  html, body { width: 848px; height: 1200px; overflow: hidden; background: var(--sheet); }
  body { position: relative; font-family: "Roboto", Arial, sans-serif; }

  .sheet-label {
    position: absolute; left: 36px; top: 65px;
    font-size: 12px; font-weight: 300; color: var(--rule); letter-spacing: .1px;
  }
  .sheet-rule { position: absolute; left: 36px; top: 87px; width: 776px; height: 1px; background: var(--rule); }

  .card {
    position: absolute; background: var(--card); overflow: hidden;
    box-shadow: 0 2px 4px rgba(0,0,0,.12);
  }
  .card--front { left: 35px; top: 133px; width: 786px; height: 490px; }
  .card--back  { left: 36px; top: 677px; width: 777px; height: 485px; }

  .brand { position: absolute; z-index: 2; display: flex; align-items: center; gap: 8px; color: var(--ink); font-weight: 500; }
  .brand__dot { width: 38px; height: 38px; border-radius: 50%; background: var(--sun); flex: none; }
  .brand__name { line-height: 1; }
  .brand__main { display: block; font-size: 25px; letter-spacing: -.3px; }
  .brand__sub  { display: block; font-size: 13px; letter-spacing: 4.2px; margin-top: 3px; padding-left: 6px; }
  .card--front .brand { left: 48px; top: 35px; }
  .card--back .brand  { left: 48px; top: 30px; }

  .photo {
    position: absolute; left: 440px; top: 0; width: 346px; height: 490px; z-index: 1;
    background: linear-gradient(160deg, #d9d9d9 0%, #8c8c8c 40%, #4a4a4a 75%, #3a3a3a 100%);
    clip-path: polygon(0 0, 100% 0, 100% 100%, 78px 100%, 66px 240px, 62px 150px, 36px 100px, 8px 40px);
  }
  .band { position: absolute; left: 0; height: 18px; background: var(--sun); }
  .card--front .band { bottom: 0; width: 520px; }
  .card--back .band  { bottom: 0; width: 100%; height: 17px; }

  .headline {
    position: absolute; left: 48px; top: 112px; z-index: 2;
    font-family: "Montserrat", Arial, sans-serif; font-weight: 800;
    font-size: 58px; line-height: 66px; color: var(--sun); letter-spacing: -1.5px;
    white-space: nowrap;
  }
  .subhead {
    position: absolute; left: 52px; top: 252px; z-index: 2; white-space: nowrap;
    font-size: 21.5px; font-weight: 500; color: var(--slate); letter-spacing: -.2px;
  }
  .perks { position: absolute; left: 52px; top: 296px; z-index: 2; white-space: nowrap; font-size: 17px; font-weight: 500; color: var(--ink); line-height: 22px; }
  .perks .sep { color: var(--sun); margin: 0 7px; }

  .contact { position: absolute; top: 386px; z-index: 2; white-space: nowrap; }
  .contact__title { font-size: 24px; font-weight: 500; color: var(--sun); line-height: 28px; }
  .contact__value { font-size: 19px; font-weight: 500; color: var(--slate); margin-top: 4px; }
  .contact--call { left: 52px; }
  .contact--web  { left: 219px; }
  .contact-divider { position: absolute; left: 198px; top: 392px; width: 1px; height: 46px; background: var(--mist); }

  .return-address {
    position: absolute; left: 291px; top: 41px;
    font-size: 12.5px; font-weight: 300; color: var(--slate); line-height: 15px;
  }
  .divider-mark { position: absolute; left: 424px; top: 48px; }
  .divider-line { position: absolute; left: 431px; top: 71px; width: 1px; height: 357px; background: var(--sun); }
  .stamp-box { position: absolute; left: 651px; top: 29px; width: 89px; height: 105px; border: 1px solid var(--sun); }

  .footer-contacts {
    position: absolute; left: 50px; top: 443px; display: flex; gap: 16px; white-space: nowrap;
    font-size: 11px; font-weight: 300; color: var(--slate);
  }
  .footer-contacts li { list-style: none; display: flex; align-items: center; gap: 5px; }
  .tagline {
    position: absolute; left: 432px; top: 443px; display: flex; align-items: center; gap: 16px; white-space: nowrap;
    font-size: 11px; font-weight: 400; color: var(--sun); text-transform: uppercase;
  }
</style>
</head>
<body>
  <p class="sheet-label">SUMMITLINE BROADBAND_CARD3</p>
  <div class="sheet-rule"></div>

  <section class="card card--front">
    <div class="photo" role="img" aria-label="Black and white portrait of a bearded young man in glasses and a denim shirt, looking up"></div>

    <div class="brand">
      <span class="brand__dot"></span>
      <span class="brand__name"><span class="brand__main">SUMMITLINE</span><span class="brand__sub">BROADBAND</span></span>
    </div>

    <h1 class="headline">BETTER,<br>NOT BIGGER!</h1>
    <p class="subhead">IT’S TIME FOR FAST, RELIABLE INTERNET</p>
    <p class="perks">
      Free residential Installation<span class="sep">|</span>In-House Tech Support<br>
      10, 25 and 40Mbps<span class="sep">|</span>Prices start at $59.95
    </p>

    <div class="contact contact--call">
      <p class="contact__title">CALL NOW!</p>
      <p class="contact__value">1 888 555 0142</p>
    </div>
    <div class="contact-divider"></div>
    <div class="contact contact--web">
      <p class="contact__title">MAIL</p>
      <p class="contact__value">www.summitline.net</p>
    </div>

    <div class="band"></div>
  </section>

  <section class="card card--back">
    <div class="brand">
      <span class="brand__dot"></span>
      <span class="brand__name"><span class="brand__main">SUMMITLINE</span><span class="brand__sub">BROADBAND</span></span>
    </div>

    <p class="return-address">PO BOX 4410<br>RIDGEFORD, CO81611</p>
    <svg class="divider-mark" width="10" height="10" viewBox="0 0 10 10"><path d="M8 1 L2 5 L8 9" fill="none" stroke="var(--sun)" stroke-width="2"/></svg>
    <div class="divider-line"></div>
    <div class="stamp-box"></div>

    <ul class="footer-contacts">
      <li>
        <svg width="11" height="11" viewBox="0 0 24 24"><path d="M6.6 10.8a15 15 0 0 0 6.6 6.6l2.2-2.2a1 1 0 0 1 1-.25 11.4 11.4 0 0 0 3.6.6 1 1 0 0 1 1 1V20a1 1 0 0 1-1 1A17 17 0 0 1 3 4a1 1 0 0 1 1-1h3.5a1 1 0 0 1 1 1c0 1.25.2 2.45.6 3.6a1 1 0 0 1-.25 1z" fill="var(--sun)"/></svg>
        1 888 555 0142
      </li>
      <li>
        <svg width="13" height="10" viewBox="0 0 26 20"><rect x="0" y="0" width="26" height="20" fill="var(--sun)"/><path d="M1 1 L13 11 L25 1" fill="none" stroke="#fff" stroke-width="2"/></svg>
        hello@summitline.net
      </li>
      <li>
        <svg width="12" height="12" viewBox="0 0 24 24"><circle cx="12" cy="12" r="4" fill="none" stroke="var(--sun)" stroke-width="3"/><path d="M16 8v5.5a3 3 0 0 0 6 0V12a10 10 0 1 0-4 8" fill="none" stroke="var(--sun)" stroke-width="3"/></svg>
        www.summitline.net
      </li>
    </ul>

    <p class="tagline">
      <svg width="9" height="10" viewBox="0 0 9 10"><path d="M1 0 L9 5 L1 10 L3 5 Z" fill="var(--sun)"/></svg>
      It’s time for fast, reliable internet.
    </p>

    <div class="band"></div>
  </section>
</body>
</html>
```